Announcement Card

This will be an announcement card mailed to clients as a postcard. The text should be oriented book fashion (not landscape).

Text is:

DEREK T. HOLLOWAN

is pleased to announce
he is joining

BRIARCREST LAW GROUP

as a founding partner

[PHONE, ADDRESS, EMAIL]

Industry/Entity Type

Fashion

```html
<!DOCTYPE html>
<html lang="en">
<head>
<meta charset="utf-8">
<title>Briarcrest Law Group – Announcement Card</title>
<link rel="stylesheet" href="https://fonts.googleapis.com/css2?family=Crimson+Pro:wght@400;600;700&display=swap">
<style>
  :root {
    --backdrop: #000000;
    --paper: #ffffff;
    --crimson: #7b1e20;
    --slate: #5b6670;
    --rule-light: #b9bec3;
    --serif: "Crimson Pro", Georgia, serif;
  }
  * { margin: 0; padding: 0; box-sizing: border-box; }
  html, body { width: 1200px; height: 1000px; overflow: hidden; background: var(--backdrop); }
  .canvas { position: relative; width: 1200px; height: 1000px; font-family: var(--serif); }

  /* Front of card */
  .card-front {
    position: absolute; left: 402px; top: 42px; width: 390px; height: 503px;
    background: var(--paper); text-align: center;
  }
  .announcer {
    position: absolute; top: 30px; left: 0; right: 0;
    font-size: 33px; font-weight: 600; color: var(--crimson); letter-spacing: 0.3px;
  }
  .announce-line {
    position: absolute; left: 0; right: 0;
    font-size: 16px; color: var(--slate); letter-spacing: 1.2px; line-height: 22px;
  }
  .announce-line.intro { top: 70px; }
  .announce-line.role { top: 308px; }
  .divider {
    position: absolute; left: 167px; width: 57px; height: 6px; background: var(--slate);
  }
  .divider.upper { top: 118px; }
  .divider.lower { top: 335px; }

  .firm-mark {
    position: absolute; left: 175px; top: 170px; width: 40px; height: 40px;
    border-radius: 50%; background: var(--crimson);
  }
  .firm-name {
    position: absolute; left: 0; right: 0; top: 240px;
    font-size: 36px; font-weight: 600; color: var(--crimson); line-height: 34px; letter-spacing: 0.5px;
  }
  .firm-name .firm-sub { display: block; font-size: 21px; letter-spacing: 2.5px; line-height: 26px; }

  .contact-front {
    position: absolute; left: 0; right: 0; top: 380px; color: var(--slate);
  }
  .contact-front .row { font-size: 17px; line-height: 23px; }
  .contact-front .label { color: var(--crimson); font-weight: 600; }
  .contact-front .address { font-size: 12px; margin-top: 5px; }
  .front-band {
    position: absolute; left: 0; right: 0; bottom: 0; height: 40px; background: var(--crimson);
  }

  /* Back of postcard */
  .card-back {
    position: absolute; left: 344px; top: 567px; width: 503px; height: 390px; background: var(--paper);
  }
  .return-panel {
    position: absolute; left: 0; top: 0; width: 243px; height: 390px;
    background: var(--crimson); color: var(--paper); text-align: center;
  }
  .return-panel .firm-mark {
    left: 104px; top: 52px; width: 34px; height: 34px; background: var(--paper);
  }
  .return-panel .firm-name {
    top: 110px; color: var(--paper); font-size: 29px; line-height: 28px;
  }
  .return-panel .firm-name .firm-sub { font-size: 15px; line-height: 20px; }
  .return-address { position: absolute; left: 0; right: 0; top: 208px; line-height: 18px; }
  .return-address .name { font-size: 21px; line-height: 26px; }
  .return-address .firm { font-size: 13px; }
  .return-address .row { font-size: 14px; }
  .return-address .label { font-weight: 700; }

  .stamp-box {
    position: absolute; left: 393px; top: 30px; width: 82px; height: 82px;
    border: 1px solid var(--rule-light);
  }
  .address-line {
    position: absolute; left: 255px; width: 220px; height: 1px; background: var(--rule-light);
  }
</style>
</head>
<body>
<main class="canvas">

  <section class="card-front" aria-label="Announcement card front">
    <h1 class="announcer">DEREK T. HOLLOWAN</h1>
    <p class="announce-line intro">IS PLEASED TO ANNOUNCE<br>HE IS JOINING</p>
    <div class="divider upper"></div>

    <div class="firm-mark"></div>
    <p class="firm-name">BRIARCREST<span class="firm-sub">LAW GROUP</span></p>

    <p class="announce-line role">AS A FOUNDING PARTNER</p>
    <div class="divider lower"></div>

    <div class="contact-front">
      <p class="row"><span class="label">phone -</span> (415) 555-0148</p>
      <p class="row"><span class="label">email</span> &nbsp;- &nbsp;derek@briarcrestlg.com</p>
      <p class="address">240 Harbor Lane, Suite 810, San Francisco, California 94111.</p>
    </div>
    <div class="front-band"></div>
  </section>

  <section class="card-back" aria-label="Postcard mailing side">
    <div class="return-panel">
      <div class="firm-mark"></div>
      <p class="firm-name">BRIARCREST<span class="firm-sub">LAW GROUP</span></p>
      <div class="return-address">
        <p class="name">DEREK T. HOLLOWAN</p>
        <p class="firm">BRIARCREST LAW GROUP</p>
        <p class="row"><span class="label">phone</span> - (415) 555-0148</p>
        <p class="row"><span class="label">email</span> - derek@briarcrestlg.com</p>
        <p class="row">240 Harbor Lane, Suite 810,</p>
        <p class="row">San Francisco, California 94111.</p>
      </div>
    </div>
    <div class="stamp-box"></div>
    <div class="address-line" style="top:180px"></div>
    <div class="address-line" style="top:224px"></div>
    <div class="address-line" style="top:271px"></div>
  </section>

</main>
</body>
</html>
```